VitaBrovo Web Design. Health and Wellness Industry

We are in process of creating next big Cloud based Health Care Management system. We have created 1st draft of Landing Page design. It is missing curb appeal, jazzy feel and engaging modern look.

Need a talented designer to recreate UI/ UX and take it to the next level.
If you are a creative designer, gifted with vision and imagination, I strongly encourage you to participate.

I want the designers to stay focus on the Landing page
Once we select the winner we will provide other subsequent pages
Follow up pages will be similar simple design

Target Market(s)

Individual Users and small business
Age Group 35-75
Individuals involved in "Health and Fitness" activity tracking, managing etc.

Industry/Entity Type

Health And Wellness

Number of Pages Required

5+ page

Colors
f68e4e
34a6d7

Requirements
Must have
• Super Engaging UI/ UX
• Smart and Contemporary look
• Easy to Navigate
• Folder Style menu bar
• Slideshow
• Social Medial Friendly
• Online Shopping
Nice to have
• Start from the enclosed draft Landing Page Idea.
• Feel Free to include additional frame, information section, Icon etc.

```html
<!DOCTYPE html>
<html lang="en">
<head>
<meta charset="utf-8">
<title>VitaBrovo — Health Management</title>
<link href="https://fonts.googleapis.com/css2?family=Open+Sans:wght@300;400;600;700&display=swap" rel="stylesheet">
<style>
:root{
  --orange:#f68e4e;
  --orange-deep:#ef7a2f;
  --blue:#34a6d7;
  --ink:#333333;
  --muted:#777777;
  --line:#e3e3e3;
  --band:#efefef;
  --dark:#1e1e1e;
  --white:#ffffff;
}
*{box-sizing:border-box;margin:0;padding:0}
html,body{width:1200px;height:2760px;overflow:hidden}
body{font-family:"Open Sans",Arial,sans-serif;color:var(--ink);background:var(--white);font-size:14px;line-height:1.6}
.section-title{font-size:28px;font-weight:700;color:var(--orange);text-align:center;letter-spacing:1px;text-transform:uppercase}
.title-rule{width:70px;height:2px;background:var(--orange);margin:8px auto 0}

/* header */
.site-header{height:112px;display:flex;align-items:center;justify-content:space-between;padding:0 120px}
.brand{display:flex;align-items:center;gap:12px;font-size:40px;font-weight:700;color:var(--orange)}
.brand-dot{width:34px;height:34px;border-radius:50%;background:var(--orange)}
.main-nav{display:flex;align-items:center;gap:4px}
.main-nav a{font-size:13px;font-weight:600;color:var(--ink);text-decoration:none;padding:9px 16px;text-transform:uppercase}
.main-nav a.active{background:var(--orange);color:var(--white)}
.search-btn{width:36px;height:36px;background:var(--orange);display:flex;align-items:center;justify-content:center;margin-left:10px}

/* hero */
.hero{position:relative;height:528px;background:linear-gradient(100deg,#4a4d4c 0%,#6d7470 40%,#a9ada3 70%,#8c8f82 100%)}
.hero-copy{position:absolute;left:150px;top:110px;color:var(--white)}
.hero-title{font-size:78px;font-weight:400;letter-spacing:4px;line-height:1}
.hero-sub{font-size:44px;font-weight:300;letter-spacing:2px;margin-top:6px;line-height:1.1}
.hero-text{font-size:15px;width:420px;margin-top:20px;line-height:1.5}
.btn-orange{display:inline-block;background:var(--orange);color:var(--white);font-size:12px;font-weight:700;padding:9px 20px;margin-top:26px;text-transform:uppercase}

/* welcome */
.welcome{height:260px;padding-top:40px;text-align:center}
.welcome p{width:1080px;margin:26px auto 0;font-size:13.5px;color:var(--muted);line-height:1.75}

/* features */
.features{height:365px;background:var(--band);display:flex;justify-content:center;gap:45px;padding-top:28px}
.feature-card{width:300px;height:300px;background:var(--white);position:relative;text-align:center}
.feature-photo{height:128px;background:linear-gradient(135deg,#cfd6dc,#8e979f)}
.feature-photo.mono{background:linear-gradient(135deg,#d8d8d8,#8a8a8a)}
.feature-icon{position:absolute;left:115px;top:90px;width:70px;height:70px;border-radius:50%;background:#555;border:4px solid var(--white);display:flex;align-items:center;justify-content:center}
.feature-icon.hot{background:var(--orange)}
.feature-card h3{font-size:14px;font-weight:700;margin-top:42px;text-transform:uppercase}
.feature-card h3.hot{color:var(--orange)}
.feature-card p{font-size:12px;color:var(--muted);padding:6px 26px 0;line-height:1.55}
.feature-go{position:absolute;left:136px;bottom:-14px;width:28px;height:28px;border-radius:50%;background:#444;display:flex;align-items:center;justify-content:center}
.feature-go.hot{background:var(--orange)}

/* news */
.news{height:335px;padding-top:40px}
.news-list{display:flex;justify-content:center;margin-top:30px}
.news-item{width:510px;display:flex;gap:20px;padding:0 30px}
.news-item + .news-item{border-left:1px solid var(--line)}
.news-date{text-align:center;width:60px;flex:none}
.news-date .day{font-size:52px;font-weight:300;line-height:1;color:var(--orange)}
.news-date .day.dark{color:var(--ink)}
.news-date .month{font-size:12px;font-weight:600;text-transform:uppercase}
.news-item h4{font-size:17px;font-weight:600;color:var(--orange);line-height:1.3}
.news-item h4.dark{color:var(--ink)}
.news-item p{font-size:12px;color:var(--muted);margin-top:10px;line-height:1.6}
.btn-outline{display:inline-block;border:1px solid #bbb;font-size:11px;padding:4px 14px;margin-top:14px;color:var(--ink)}

/* team */
.team{height:420px;background:var(--orange-deep);padding-top:36px}
.team .section-title{color:var(--white)}
.team .title-rule{background:var(--white)}
.team-grid{display:flex;justify-content:center;gap:24px;margin-top:36px}
.member{width:222px;background:var(--white)}
.member-photo{height:190px;background:linear-gradient(160deg,#bfb2a5,#6e6258)}
.member-photo.cool{background:linear-gradient(160deg,#b9bcc2,#5d6068)}
.member-name{font-size:14px;font-weight:700;color:var(--orange);text-align:center;padding:12px 0 4px;text-transform:uppercase}
.member-role{font-size:11px;color:var(--muted);text-align:center;padding-bottom:12px}

/* clients */
.clients{height:300px;padding-top:36px;text-align:center;position:relative}
.quote-mark{position:absolute;font-size:90px;font-weight:700;color:var(--orange);line-height:1}
.clients p{width:880px;margin:30px auto 0;font-size:13px;color:var(--muted);line-height:1.75}
.client{display:flex;align-items:center;justify-content:center;gap:14px;margin-top:20px}
.client-avatar{width:52px;height:52px;border-radius:50%;background:linear-gradient(135deg,#c9a58f,#6b4a3c)}
.client-name{font-size:13px;font-weight:700;color:var(--orange);text-transform:uppercase}

/* contact */
.contact{height:400px;background:linear-gradient(180deg,#262626,#161616);padding-top:36px;color:#cfcfcf}
.contact .section-title{color:var(--white)}
.contact .title-rule{background:var(--white)}
.contact-body{display:flex;justify-content:space-between;width:960px;margin:38px auto 0}
.contact-info{width:380px;font-size:13px}
.contact-row{display:flex;gap:14px;align-items:flex-start;margin-bottom:20px;line-height:1.5}
.contact-row svg{flex:none;margin-top:2px}
.social{display:flex;gap:12px;margin-top:24px}
.social span{width:34px;height:34px;border-radius:50%;background:#555}
.social span.hot{background:var(--orange)}
.contact-form{width:500px}
.field-row{display:flex;gap:14px}
.field{flex:1;height:36px;border:1px solid #555;font-size:12px;color:#999;padding:8px 12px;margin-bottom:14px}
.field.message{height:110px}
.btn-send{background:var(--orange);color:var(--white);font-size:14px;font-weight:600;letter-spacing:2px;text-align:center;padding:9px 0;text-transform:uppercase}

/* footer */
.site-footer{height:40px;display:flex;align-items:center;justify-content:center;font-size:11px;color:var(--muted)}
</style>
</head>
<body>

<header class="site-header">
  <div class="brand"><span class="brand-dot"></span>VitaBrovo</div>
  <nav class="main-nav">
    <a class="active">Home</a>
    <a>Discover Healthdaily</a>
    <a>Shop</a>
    <a>Caregiver</a>
    <a>Community</a>
    <span class="search-btn"><svg width="16" height="16" viewBox="0 0 16 16"><circle cx="6.5" cy="6.5" r="4.8" fill="none" stroke="#fff" stroke-width="2"/><line x1="10" y1="10" x2="14.5" y2="14.5" stroke="#fff" stroke-width="2"/></svg></span>
  </nav>
</header>

<section class="hero" role="img" aria-label="Photo of a woman in a red sports top doing push-ups on an outdoor path">
  <div class="hero-copy">
    <h1 class="hero-title">VITA BROVO</h1>
    <div class="hero-sub">HEALTH MANAGMENT</div>
    <p class="hero-text">Lorem ipsum dolor sit amet consectetur adipiscing elit. Nulla vel viverra massa sed rhoncus.</p>
    <span class="btn-orange">Read More</span>
  </div>
</section>

<section class="welcome">
  <h2 class="section-title">Welcome to VitaBrovo</h2>
  <div class="title-rule"></div>
  <p>Lorem ipsum dolor sit amet, consectetur adipiscing elit. Suspendisse vel magna et risus fringilla faucibus. Nam at tincidunt tellus, a vehicula enim. Duis in iaculis risus. Quisque porttitor elit sit amet lorem sollicitudin, et dignissim libero imperdiet. Aenean ante lacus, ultricies id feugiat eu, convallis quis mauris. Aliquam et placerat velit. Morbi cursus commodo ipsum. Etiam facilisis sollicitudin quam, vitae vestibulum tortor tincidunt a. Nulla tincidunt, nisl ac placerat elementum, neque nisi hendrerit lectus, vel sodales magna velit sed nulla. Praesent lobortis justo eget tortor rutrum, at aliquet magna semper.</p>
</section>

<section class="features">
  <article class="feature-card">
    <div class="feature-photo" role="img" aria-label="Photo of a medical team in discussion"></div>
    <div class="feature-icon hot"><svg width="30" height="30" viewBox="0 0 30 30" fill="none" stroke="#fff" stroke-width="2"><ellipse cx="15" cy="7" rx="10" ry="4"/><path d="M5 7v16c0 2.2 4.5 4 10 4s10-1.8 10-4V7"/><path d="M5 15c0 2.2 4.5 4 10 4s10-1.8 10-4"/></svg></div>
    <h3 class="hot">Products</h3>
    <p>Efficient and dynamic product lines for modern health tracking and everyday care at home.</p>
    <span class="feature-go hot"><svg width="10" height="10" viewBox="0 0 10 10"><path d="M3 1l4 4-4 4" fill="none" stroke="#fff" stroke-width="2"/></svg></span>
  </article>
  <article class="feature-card">
    <div class="feature-photo mono" role="img" aria-label="Photo of a support agent wearing a headset"></div>
    <div class="feature-icon"><svg width="30" height="30" viewBox="0 0 30 30" fill="none" stroke="#fff" stroke-width="2"><rect x="4" y="5" width="22" height="15" rx="1"/><line x1="15" y1="20" x2="15" y2="25"/><line x1="9" y1="25" x2="21" y2="25"/></svg></div>
    <h3>Lorem Ipsum Dolor Sit</h3>
    <p>Sed placerat mauris at ultricies iaculis, varius tortor quis elit nulla posuere lacus in nibh.</p>
    <span class="feature-go"><svg width="10" height="10" viewBox="0 0 10 10"><path d="M3 1l4 4-4 4" fill="none" stroke="#fff" stroke-width="2"/></svg></span>
  </article>
  <article class="feature-card">
    <div class="feature-photo mono" role="img" aria-label="Photo of hands typing on a laptop keyboard"></div>
    <div class="feature-icon"><svg width="30" height="30" viewBox="0 0 30 30" fill="none" stroke="#fff" stroke-width="2"><rect x="7" y="13" width="16" height="12" rx="1"/><path d="M10 13V9a5 5 0 0 1 10 0v4"/><circle cx="15" cy="19" r="1.5" fill="#fff"/></svg></div>
    <h3>Ipsum Dolor Sit Amet</h3>
    <p>Donec vitae tortor eget nunc mattis feugiat, integer posuere dui sed velit cursus et mollis.</p>
    <span class="feature-go"><svg width="10" height="10" viewBox="0 0 10 10"><path d="M3 1l4 4-4 4" fill="none" stroke="#fff" stroke-width="2"/></svg></span>
  </article>
</section>

<section class="news">
  <h2 class="section-title">Latest News</h2>
  <div class="title-rule"></div>
  <div class="news-list">
    <article class="news-item">
      <div class="news-date"><div class="day">11</div><div class="month">June</div></div>
      <div>
        <h4>Lorem ipsum dolor sit ameta loramer elit.</h4>
        <p>Lorem ipsum dolor sit amet, consectetur adipiscing elit. Aenean ut nisi tempor, luctus tellus vitae, commodo massa. Sed non lectus at lorem aliquet finibus.</p>
        <span class="btn-outline">Read More</span>
      </div>
    </article>
    <article class="news-item">
      <div class="news-date"><div class="day dark">15</div><div class="month">June</div></div>
      <div>
        <h4 class="dark">Lorem ipsum dolor sit ameta loramer elit.</h4>
        <p>Lorem ipsum dolor sit amet, consectetur adipiscing elit. Donec blandit semper tempor, tortor augue pretium ante, nec volutpat odio lacus vel purus.</p>
        <span class="btn-outline">Read More</span>
      </div>
    </article>
  </div>
</section>

<section class="team">
  <h2 class="section-title">Our Team</h2>
  <div class="title-rule"></div>
  <div class="team-grid">
    <div class="member"><div class="member-photo" role="img" aria-label="Portrait photo of a team member"></div><div class="member-name">Ipsun Lorem</div><div class="member-role">Lorem ipsum dolor</div></div>
    <div class="member"><div class="member-photo cool" role="img" aria-label="Portrait photo of a team member"></div><div class="member-name">Paudolor Sitetur</div><div class="member-role">Lorem ipsum dolor</div></div>
    <div class="member"><div class="member-photo" role="img" aria-label="Portrait photo of a team member"></div><div class="member-name">Holobitl Orenum</div><div class="member-role">Lorem ipsum dolor</div></div>
    <div class="member"><div class="member-photo cool" role="img" aria-label="Portrait photo of a team member"></div><div class="member-name">Ameton Sectetur</div><div class="member-role">Lorem ipsum dolor</div></div>
  </div>
</section>

<section class="clients">
  <h2 class="section-title">Happy Clients</h2>
  <div class="title-rule"></div>
  <span class="quote-mark" style="left:130px;top:110px">&ldquo;</span>
  <p>Lorem Suspendisse ac eleifend risus. Praesent vel erat quis arcu placerat tincidunt dictum. Nulla fermentum tortor a mauris eget feugiat, varius quis libero tristique. Cras eget lectus tempus, lacinia arcu nec, facilisis justo. Maecenas volutpat dolor pharetra lacus rutrum, nec ornare nunc pretium. Donec luctus blandit vulputate sed ut ante.</p>
  <span class="quote-mark" style="right:130px;top:170px">&rdquo;</span>
  <div class="client"><div class="client-avatar" role="img" aria-label="Small portrait photo of a client"></div><div class="client-name">Lorem Ipsum Dol</div></div>
</section>

<section class="contact">
  <h2 class="section-title">Get in Touch</h2>
  <div class="title-rule"></div>
  <div class="contact-body">
    <div class="contact-info">
      <div class="contact-row"><svg width="14" height="18" viewBox="0 0 14 18"><path d="M7 1a6 6 0 0 0-6 6c0 4.5 6 10 6 10s6-5.5 6-10a6 6 0 0 0-6-6z" fill="#888"/><circle cx="7" cy="7" r="2.2" fill="#222"/></svg><span>48 Marlow Crescent, Fenbridge<br>Suite 210, North Quarter 40718</span></div>
      <div class="contact-row"><svg width="16" height="16" viewBox="0 0 16 16"><path d="M3 1l3 1 1 3-2 1.5a9 9 0 0 0 4.5 4.5L11 9l3 1 1 3-2 2C7 15 1 9 1 3z" fill="#888"/></svg><span>+1 555 0142 778</span></div>
      <div class="contact-row"><svg width="16" height="14" viewBox="0 0 16 14"><rect x="1" y="2" width="14" height="10" fill="none" stroke="#888" stroke-width="1.5"/><path d="M1 2l7 6 7-6" fill="none" stroke="#888" stroke-width="1.5"/></svg><span>care@vitabrovo.example</span></div>
      <div class="social"><span class="hot"></span><span></span><span></span><span></span></div>
    </div>
    <div class="contact-form">
      <div class="field-row"><div class="field">Your Name...</div><div class="field">Your email@...</div></div>
      <div class="field message">Message...</div>
      <div class="btn-send">Send Massage</div>
    </div>
  </div>
</section>

<footer class="site-footer">Copyright © 2015 VitaBrovo. All rights reserved.</footer>

</body>
</html>
```